Boutique Film/TV Company needs Business Card Design

Please see our website for background on our company and look of our current logo: www.lumarocpictures.ca

Pantone 314U is our main colour.

Target Market(s)

Network of peers, funders and broadcasters.

Industry/Entity Type

Business

Requirements
Must have
• We would like rounded corners and the height of the card to be shorter than traditional (maybe?!)

It's important that we have room for our office address, office number, cell number, email address, website, facebook and linked-in info (though not all of us have a linked-in account).

Would like the logo to keep the exclamation marks over the letters but the tag line/tag words of "film - television - interactive" can stay or go or... surprise me!

Nice to have
• Silky matte finish.

We are open to a change in the font of our logo/name.

```html
<!DOCTYPE html>
<html lang="en">
<head>
<meta charset="utf-8">
<title>Lumaroc Pictures — Business Card</title>
<link rel="stylesheet" href="https://fonts.googleapis.com/css2?family=Marcellus&family=Open+Sans:wght@700&display=swap">
<style>
  :root {
    --backdrop: #3a3a3a;
    --card-glow: #00e6ee;
    --card-mid: #0aa6cf;
    --card-edge: #0a6ea8;
    --ink: #ffffff;
    --ghost-word: rgba(120, 170, 205, 0.42);
  }
  html, body {
    margin: 0;
    width: 1200px;
    height: 785px;
    overflow: hidden;
    background: var(--backdrop);
  }
  .stage {
    position: relative;
    width: 1200px;
    height: 785px;
  }
  .card {
    position: absolute;
    top: 246px;
    width: 473px;
    height: 287px;
    filter: drop-shadow(0 3px 5px rgba(0, 0, 0, 0.45));
  }
  .card--front { left: 116px; }
  .card--back { left: 618px; }
  .ghost-word {
    font-family: "Open Sans", Verdana, sans-serif;
    font-weight: 700;
    fill: var(--ghost-word);
  }
  .wordmark {
    font-family: "Marcellus", serif;
    fill: var(--ink);
  }
  .person-name {
    font-family: "Marcellus", serif;
    font-size: 24px;
    fill: var(--ink);
  }
  .person-role {
    font-family: "Marcellus", serif;
    font-size: 10.5px;
    fill: var(--ink);
  }
  .contact {
    font-family: "Marcellus", serif;
    fill: var(--ink);
  }
  .contact--large { font-size: 13px; }
  .contact--mid { font-size: 12px; }
  .contact--small { font-size: 10.5px; letter-spacing: 0.2px; }
  .icon { fill: var(--ink); }
  .icon-line { fill: none; stroke: var(--ink); stroke-width: 1; }
</style>
</head>
<body>
<main class="stage">

  <!-- Front of card -->
  <svg class="card card--front" viewBox="0 0 473 287" xmlns="http://www.w3.org/2000/svg">
    <defs>
      <radialGradient id="front-fill" cx="0.42" cy="0.55" r="0.75">
        <stop offset="0" stop-color="var(--card-glow)"/>
        <stop offset="0.5" stop-color="var(--card-mid)"/>
        <stop offset="1" stop-color="var(--card-edge)"/>
      </radialGradient>
    </defs>
    <rect width="473" height="287" rx="28" fill="url(#front-fill)"/>
    <text class="ghost-word" x="75" y="66" font-size="42">Television</text>
    <text class="ghost-word" x="20" y="101" font-size="30">Films</text>
    <text class="ghost-word" x="122" y="133" font-size="50">Interactive</text>
    <text class="wordmark" x="430" y="253" font-size="70" text-anchor="end">Lumaroc</text>
  </svg>

  <!-- Back of card -->
  <svg class="card card--back" viewBox="0 0 473 287" xmlns="http://www.w3.org/2000/svg">
    <defs>
      <radialGradient id="back-fill" cx="0.45" cy="0.5" r="0.8">
        <stop offset="0" stop-color="var(--card-glow)"/>
        <stop offset="0.5" stop-color="var(--card-mid)"/>
        <stop offset="1" stop-color="var(--card-edge)"/>
      </radialGradient>
    </defs>
    <rect width="473" height="287" rx="28" fill="url(#back-fill)"/>
    <text class="ghost-word" x="118" y="78" font-size="42">Television</text>
    <text class="ghost-word" x="66" y="108" font-size="28">Films</text>
    <text class="ghost-word" x="162" y="136" font-size="50">Interactive</text>
    <text class="wordmark" x="444" y="64" font-size="44" text-anchor="end">Lumaroc</text>

    <text class="person-name" x="36" y="155">DANIEL REYES</text>
    <text class="person-role" x="36" y="171">Head of Development, Drama and Scripted Content</text>
    <line x1="36" y1="177.5" x2="444" y2="177.5" stroke="#ffffff" stroke-width="1"/>

    <!-- address -->
    <path class="icon" d="M40 193 l5 -5 l5 5 h-1.5 v4.5 h-2.5 v-3 h-2 v3 h-2.5 v-4.5 z"/>
    <text class="contact contact--large" x="53" y="197">48 Alder Crescent, Toronto, ON  M4K 2P8</text>
    <!-- office phone -->
    <path class="icon" d="M40.5 206 q1.5 -1.5 3 0 l1 1.5 q0.3 0.8 -0.6 1.4 q1 2 3 3 q0.6 -0.9 1.4 -0.6 l1.5 1 q1.5 1.5 0 3 q-3 1 -6.5 -2.6 q-3.6 -3.5 -2.8 -6.7 z"/>
    <text class="contact contact--mid" x="53" y="213">+ 416.555.0172</text>
    <!-- mobile -->
    <rect class="icon" x="42" y="221" width="6" height="10" rx="1"/>
    <rect x="43" y="222.5" width="4" height="4.5" fill="#0a8fc2"/>
    <text class="contact contact--mid" x="53" y="230">+ 416.555.0172</text>
    <!-- email -->
    <path class="icon" d="M40 241 l5 -3.5 l5 3.5 v4.5 h-10 z"/>
    <path class="icon-line" d="M40.5 241.5 l4.5 3 l4.5 -3"/>
    <text class="contact contact--small" x="53" y="246">INFO@LUMAROCPICTURES.CA</text>
    <!-- web -->
    <circle class="icon-line" cx="45" cy="257" r="4.5"/>
    <ellipse class="icon-line" cx="45" cy="257" rx="2" ry="4.5"/>
    <line class="icon-line" x1="40.5" y1="257" x2="49.5" y2="257"/>
    <text class="contact contact--small" x="53" y="261">WWW.LUMAROCPICTURES.CA</text>
  </svg>

</main>
</body>
</html>
```